Website for my photography business

I need a website for my photography business, Jonah Pelling Photography. I need a website that has a landing page with a cover photo of each kind of photography I do. For example, Nature, Weddings, Portraits and Architecture. I want it so that when someone comes onto my website they have to choose which kind of photography page they want to visit. So if they click on the wedding photo it will open to a page with my wedding portfolio images and a contact me button. If they choose nature photography I want them to be redirected to an e-commerce section where they can purchase prints. Architecture and Portraits should open up to their respective portfolios with about me and contact info. I like this kind of format because I want people who come to my website for a specific type of photography to be able to be directed there easily without having to look at a mix of other kinds of photography. I will provide a few files to use as placeholders. I have already purchased the jonahpellingphotography.example domain name. A Wix website would be great because I am most familiar with it but I am open to anything.

Industry/Entity Type

Photographer

Number of Pages Required

5+ page

Requirements
Must have
• Landing Page and e-commerce

```html
<!DOCTYPE html>
<html lang="en">
<head>
<meta charset="utf-8">
<title>Jonah Pelling Photography</title>
<link rel="stylesheet" href="https://fonts.googleapis.com/css2?family=Playfair+Display:ital,wght@0,400;0,700;1,400&family=Poppins:wght@400;500;600&family=Cormorant+Garamond:ital,wght@0,400;1,400&display=swap">
<style>
:root{
  --ink:#1c1c1c;
  --navy:#2e3566;
  --muted:#8a8a8a;
  --line:#d9d9d9;
  --cream:#fdf9f6;
  --blush:#f8f0ec;
  --stone:#a9a69c;
  --white:#ffffff;
}
*{box-sizing:border-box;margin:0;padding:0}
html,body{width:1200px;height:2706px;overflow:hidden;background:var(--white)}
body{position:relative;font-family:"Poppins",sans-serif;color:var(--ink)}
.abs{position:absolute}
.serif{font-family:"Playfair Display",serif}
.center{text-align:center}

/* header */
.search{left:235px;top:38px;width:107px;height:26px;border-bottom:1px solid var(--line);font:italic 13px "Playfair Display",serif;color:var(--muted)}
.search svg{position:absolute;right:0;top:6px}
.nav{top:45px;font-size:9px;font-weight:500;letter-spacing:.3px}
.brand{font-family:"Playfair Display",serif;color:var(--navy);white-space:nowrap}
.cart{left:951px;top:43px}

/* slider */
.photo{position:absolute}
.ph-fox{background:linear-gradient(160deg,#2f3d33 0%,#4c5e48 40%,#c7773a 62%,#eef0f3 85%)}
.ph-ring{background:linear-gradient(140deg,#b49c86 0%,#8d7f77 45%,#223048 60%,#a28a73 100%)}
.ph-bw{background:linear-gradient(120deg,#d8d8d8 0%,#5f5f5f 50%,#2a2a2a 100%)}
.ph-arch{background:linear-gradient(170deg,#d5dee8 0%,#9e5d43 45%,#c8b49b 75%,#8f8f8f 100%)}
.pager{top:546px;left:564px;font-size:8px;font-weight:600;display:flex;align-items:center;gap:10px}
.pager span.line{width:24px;height:1px;background:var(--line)}
.pager .dim{color:var(--muted);font-weight:500}

/* about */
.about-title{top:726px;width:1200px;font-size:25px;letter-spacing:.5px}
.about-copy{left:345px;top:780px;width:510px;font-size:9.5px;line-height:17.5px}
.btn{background:var(--stone);color:var(--white);font-size:8px;font-weight:600;display:flex;align-items:center;justify-content:center}

/* categories */
.band-cream{left:0;top:958px;width:1200px;height:422px;background:var(--cream)}
.cat-label{width:168px;font:700 15px "Playfair Display",serif}

/* contact */
.sec-title{width:1200px;font-size:25px}
.form-frame{left:76px;top:1515px;width:1039px;height:450px;border:1px solid var(--line)}
.field{border-bottom:1px solid var(--line);font-size:8.5px;letter-spacing:2.5px;color:var(--muted);padding-left:2px}

/* instagram */
.band-blush{left:0;top:2261px;width:1200px;height:154px;background:var(--blush)}
.handle{width:1200px;top:2076px;font-size:15px;color:var(--muted)}
.ig-a{background:linear-gradient(180deg,#d9dbd0,#6f7757 70%,#7c6d52)}
.ig-b{background:linear-gradient(160deg,#e8e5df,#6e7f62 60%,#e0ddd6)}
.ig-c{background:linear-gradient(120deg,#a9b59a,#3c4c45 55%,#d5c9bb)}
.ig-d{background:linear-gradient(180deg,#b5b5b5,#4a4a4a 40%,#f2f2f2 85%)}
.ig-e{background:linear-gradient(180deg,#6a7b55,#d9ccc0 55%,#8b9a70)}
.ig-f{background:linear-gradient(100deg,#efefef 30%,#3b3f3a 60%,#1f1f1f)}

/* footer */
.divider{top:2457px;width:1px;height:170px;background:var(--line)}
.foot-head{font:400 17px "Cormorant Garamond",serif;letter-spacing:3.5px;color:#555;width:300px}
.soc{top:2534px;left:150px;display:flex;align-items:center;gap:10px}
.soc i{display:block;width:11px;height:11px;border-radius:50%;background:#666}
.soc span{width:24px;height:1px;background:var(--line)}
.foot-mail{left:76px;top:2566px;width:330px;font:italic 12px "Playfair Display",serif;color:#555;white-space:nowrap}
.copy-band{left:0;top:2659px;width:1200px;height:47px;background:var(--blush)}
.copy{width:1200px;top:2679px;font-size:8.5px}
</style>
</head>
<body>

<!-- header -->
<div class="abs search">Search...
  <svg width="9" height="9" viewBox="0 0 10 10"><circle cx="4" cy="4" r="3" fill="none" stroke="#333" stroke-width="1.4"/><line x1="6.3" y1="6.3" x2="9" y2="9" stroke="#333" stroke-width="1.4"/></svg>
</div>
<div class="abs nav" style="left:388px">HOME</div>
<div class="abs nav" style="left:439px">ABOUT</div>
<div class="abs brand" style="left:500px;top:40px;width:200px;text-align:center;font-size:15px">Jonah Pelling Photography</div>
<div class="abs nav" style="left:732px">PORTFOLIO</div>
<div class="abs nav" style="left:803px">SHOP</div>
<div class="abs nav" style="left:850px">CONTACT</div>
<svg class="abs cart" width="13" height="13" viewBox="0 0 13 13"><path d="M2 4h9l-1 8H3z" fill="none" stroke="#333" stroke-width="1.2"/><path d="M4.5 4V3a2 2 0 0 1 4 0v1" fill="none" stroke="#333" stroke-width="1.2"/></svg>

<!-- slider -->
<div class="photo ph-ring" style="left:0;top:102px;width:246px;height:417px" role="img" aria-label="Wedding ring resting on a speckled stone"></div>
<div class="photo ph-fox" style="left:302px;top:102px;width:595px;height:417px" role="img" aria-label="Red fox sitting in snow beneath pine trees"></div>
<div class="photo ph-bw" style="left:954px;top:102px;width:246px;height:417px" role="img" aria-label="Black and white portrait study"></div>
<div class="abs pager">01<span class="line"></span><span class="dim">04</span></div>

<!-- about -->
<div class="abs brand center" style="top:640px;width:1200px;font-size:28px">Jonah Pelling Photography</div>
<h2 class="abs serif center about-title" style="font-weight:400">ABOUT US</h2>
<p class="abs center about-copy">Lorem ipsum dolor sit amet, consectetur adipiscing elit. Aliquam a velit at ante aliquam sagittis. Aliquam aliquam fringilla lectus in blandit. Etiam odio lectus, porta a pellentesque ut, imperdiet nec tortor. Fusce finibus condimentum cursus. Quisque est arcu, placerat sed est ut, feugiat bibendum justo.</p>
<div class="abs btn" style="left:522px;top:857px;width:156px;height:34px">GET IN TOUCH</div>

<!-- categories -->
<div class="abs band-cream"></div>
<div class="photo ph-fox" style="left:234px;top:1029px;width:168px;height:216px" role="img" aria-label="Nature category cover: fox in snow"></div>
<div class="abs cat-label center" style="left:234px;top:1263px">Nature</div>
<div class="photo ph-ring" style="left:422px;top:1059px;width:168px;height:216px" role="img" aria-label="Weddings category cover: ring on stone"></div>
<div class="abs cat-label center" style="left:422px;top:1294px">Weddings</div>
<div class="photo ph-bw" style="left:609px;top:1029px;width:168px;height:216px" role="img" aria-label="Portraits category cover: black and white figure study"></div>
<div class="abs cat-label center" style="left:609px;top:1263px">Portraits</div>
<div class="photo ph-arch" style="left:798px;top:1059px;width:168px;height:216px" role="img" aria-label="Architecture category cover: brick and glass building"></div>
<div class="abs cat-label center" style="left:798px;top:1294px">Architecture</div>

<!-- contact -->
<h2 class="abs serif center sec-title" style="top:1452px;font-weight:400">GET IN TOUCH</h2>
<div class="abs form-frame"></div>
<div class="abs field" style="left:252px;top:1574px;width:332px;height:17px">NAME</div>
<div class="abs field" style="left:608px;top:1574px;width:331px;height:17px">E-MAIL</div>
<div class="abs field" style="left:252px;top:1644px;width:332px;height:17px">WEDDING DATE</div>
<div class="abs field" style="left:608px;top:1644px;width:331px;height:17px">WEDDING ADDRESS</div>
<div class="abs field" style="left:252px;top:1714px;width:687px;height:125px">TELL US MORE</div>
<div class="abs btn" style="left:509px;top:1864px;width:172px;height:38px;letter-spacing:2.5px;font-weight:500">SEND</div>

<!-- instagram -->
<div class="abs band-blush"></div>
<h2 class="abs serif center sec-title" style="top:2031px;font-weight:400">FOLLOW ME ON INSTAGRAM</h2>
<div class="abs serif center handle">@ Jonah_Pelling_Photography</div>
<div class="photo ig-a" style="left:115px;top:2200px;width:129px;height:101px" role="img" aria-label="Couple standing in a field"></div>
<div class="photo ig-b" style="left:284px;top:2162px;width:129px;height:159px" role="img" aria-label="Wedding stationery with greenery"></div>
<div class="photo ig-c" style="left:452px;top:2200px;width:129px;height:101px" role="img" aria-label="Bridesmaids in green dresses"></div>
<div class="photo ig-d" style="left:621px;top:2162px;width:129px;height:159px" role="img" aria-label="Bride and guests in black and white"></div>
<div class="photo ig-e" style="left:789px;top:2200px;width:129px;height:101px" role="img" aria-label="Bridal hairstyle with flowers"></div>
<div class="photo ig-f" style="left:957px;top:2162px;width:129px;height:159px" role="img" aria-label="Couple holding hands"></div>

<!-- footer -->
<div class="abs divider" style="left:414px"></div>
<div class="abs divider" style="left:760px"></div>
<div class="abs foot-head center" style="left:91px;top:2497px">FOLLOW US</div>
<div class="abs soc"><i></i><span></span><i></i><span></span><i></i><span></span><i></i></div>
<div class="abs foot-mail center">info@jonahpellingphotography.example</div>
<div class="abs brand center" style="left:414px;top:2522px;width:346px;font-size:22px">Jonah Pelling Photography</div>
<div class="abs foot-head center" style="left:783px;top:2497px">NEWSLETTER</div>
<div class="abs center" style="left:783px;top:2527px;width:300px;font:italic 14px 'Cormorant Garamond',serif;color:#777">Follow our latest stories.</div>
<div class="abs field" style="left:825px;top:2567px;width:221px;height:18px;font-size:8px">E-MAIL
  <svg style="position:absolute;right:2px;top:0" width="13" height="9" viewBox="0 0 13 9"><rect x=".5" y=".5" width="12" height="8" fill="none" stroke="#777"/><path d="M.5 .5l6 4.5 6-4.5" fill="none" stroke="#777"/></svg>
</div>
<div class="abs copy-band"></div>
<div class="abs copy center">Copyright © 2020 Jonah Pelling Photography. All Rights Reserved</div>

</body>
</html>
```